Safety Consultancy focusing on developing exceptional Safety Leaders

I need a full but simple, modern, catchy website to drive business - my focus is on helping organizations to understand the impact that leaders have on safety performance and how they build the processes to make that happen. I already have great branding (logos) built through PixelGuild and can provide all narrative to build out the pages

Target Market(s)

Focused internationally. Typical client has a fairly robust and mature safety culture yet lacks the focused effort to develop all levels of leadership in terms of managing safety. Exercising these competencies results in continued development of an organizations safety culture as well as improved safety performance

Industry/Entity Type

all

Coding

Coded - Design and coding required

Number of Pages Required

4 page

Font styles to use
Other font styles liked:
• to match my branding

Colors
0054AA
0677BA
7BADD7
CADEEF
E8F1F8

Requirements
Must have
• Must utilize my current branding, logo, etc. I want to have a page outlining clearly my vision - which I will add to my uploads as we move forward. I need to have a page listing my extensive and unique experience as well as successes
Nice to have
• Want to leave it up to designers - but needs to be simple and easily navigable - hope to have a resource page that I can update myself with safety resource info, reports, etc.

```html
<!DOCTYPE html>
<html lang="en">
<head>
<meta charset="utf-8">
<title>Kestrel Ventures International — Safety Consultancy</title>
<link href="https://fonts.googleapis.com/css2?family=Open+Sans:wght@400;600;700;800&display=swap" rel="stylesheet">
<style>
:root{
  --navy:#0e2a5a;
  --ink:#0f2146;
  --blue:#0677ba;
  --blue-deep:#0054aa;
  --blue-soft:#7badd7;
  --blue-pale:#cadeef;
  --bg-pale:#e8f1f8;
  --text:#5b6577;
  --footer:#163150;
  --white:#ffffff;
  --star:#f08a24;
}
*{box-sizing:border-box;margin:0;padding:0}
html,body{width:1200px;height:4320px;overflow:hidden}
body{position:relative;font-family:"Open Sans",Arial,sans-serif;color:var(--text);background:var(--white)}
.abs{position:absolute}
/* header */
.topbar{left:390px;top:0;width:810px;height:34px;background:var(--navy);border-bottom-left-radius:40px}
.topbar span{position:absolute;top:9px;font-size:11px;color:#cfd9ea}
.topbar .quote{left:470px;top:6px;background:#2f6f86;color:#fff;padding:3px 18px;font-weight:600}
.brand{display:flex;align-items:center;gap:10px}
.brand .mark{width:28px;height:28px;border-radius:50%;background:var(--blue-soft)}
.brand .name{font-weight:700;font-size:26px;color:#3a2b7a}
.nav{left:404px;top:50px;display:flex;gap:40px;font-size:12px;color:#4c5870}
.nav .active{color:var(--blue-deep);font-weight:700}
/* hero */
.hero{left:0;top:80px;width:1200px;height:750px}
.hero-title{left:129px;top:262px;font-size:44px;line-height:49px;font-weight:700;color:#fff}
.hero-text{left:129px;top:386px;width:460px;font-size:20px;line-height:28px;color:#e7eefb}
.btn{display:inline-flex;align-items:center;justify-content:center;gap:10px;background:var(--blue);color:#fff;font-weight:700;font-size:13px}
.hero-btn{left:129px;top:501px;width:154px;height:40px;border-radius:20px}
/* intro */
.pale{background:var(--bg-pale)}
.eyebrow{font-size:13px;color:var(--blue);letter-spacing:.3px;border-bottom:2px solid var(--blue);padding-bottom:4px}
.h2{font-weight:700;color:var(--ink)}
.center{text-align:center;left:0;width:1200px}
.card{width:275px;height:240px;background:#fff;box-shadow:0 6px 18px rgba(20,50,90,.1);border-bottom:4px solid var(--blue);display:flex;flex-direction:column;align-items:center;justify-content:center;gap:26px}
.card h3{font-size:22px;color:#4d5566;font-weight:700;letter-spacing:.5px}
.card p{font-size:13px;line-height:21px;text-align:center;padding:0 36px;color:#6a7284}
.card svg{stroke:var(--blue);fill:none;stroke-width:3}
/* about */
.para{font-size:12px;line-height:19px;color:#6a7284}
/* services */
.svc{top:2058px;height:451px}
.band{background:var(--navy);display:flex;align-items:flex-end;justify-content:center;padding-bottom:20px}
.band .vert{writing-mode:vertical-rl;transform:rotate(180deg);color:#fff;font-size:12px;white-space:nowrap}
.band .vert b{font-size:15px;margin-left:6px}
/* testimonials */
.avatar{border-radius:50%;background:linear-gradient(160deg,#c9d4df,#7b8797);border:4px solid #fff}
.arrow{width:44px;height:44px;border-radius:50%;display:flex;align-items:center;justify-content:center}
/* contact */
.field-label{font-size:14px;font-weight:700;color:var(--blue-deep)}
.field{border:1.5px solid #c9ccd3;font-size:12px;color:#9aa0ab;padding:12px 16px}
.info{display:flex;align-items:center;gap:24px;font-size:14px;color:#6a7284;left:140px}
.info i{width:36px;height:36px;border-radius:50%;background:#fff;box-shadow:0 2px 8px rgba(0,0,0,.1);display:flex;align-items:center;justify-content:center}
/* footer */
.foot-h{font-size:15px;font-weight:700;color:#fff}
.foot-t{font-size:12px;color:#e1e8f2;line-height:21px}
.soc{width:40px;height:40px;border:1.5px solid #fff;display:flex;align-items:center;justify-content:center}
.soc span{width:10px;height:10px;background:#fff;border-radius:2px}
</style>
</head>
<body>

<!-- header -->
<div class="abs topbar">
  <span style="left:80px">&#9679; 48 Harbor Lane, Brookfield, NY 10210</span>
  <span style="left:315px">Follow Us: &#9642; &#9642; &#9642;</span>
  <span class="quote">GET QUOTATION</span>
</div>
<div class="abs brand" style="left:122px;top:30px"><span class="mark"></span><span class="name">Kestrel</span></div>
<nav class="abs nav"><span class="active">Home</span><span>Services</span><span>About Us</span><span>Our Team</span><span>And more</span><span>Contact Us</span></nav>

<!-- hero -->
<div class="abs hero" role="img" aria-label="Photo of safety engineers in hard hats inspecting an industrial plant" style="background:linear-gradient(90deg,#0d2d6a 0%,#2b4f86 45%,#7f95b2 100%)"></div>
<svg class="abs" style="left:0;top:620px" width="1200" height="230" viewBox="0 0 1200 230">
  <path d="M0 164 C300 175 700 110 1200 0 L1200 230 L0 230Z" fill="#e8f1f8"/>
  <path d="M0 172 C300 165 600 130 820 110 C560 150 260 185 0 212Z" fill="#0677ba"/>
</svg>
<h1 class="abs hero-title">Navigating Safety<br>with Expertise</h1>
<p class="abs hero-text">Lorem ipsum dolor sit amet, consectetur adipiscing elit, sed do eiusmod tempor incidid unt ut labore et dolore magna aliqua.</p>
<a class="abs btn hero-btn">READ MORE</a>

<!-- who we are -->
<section class="abs pale" style="left:0;top:830px;width:1200px;height:571px"></section>
<div class="abs center" style="top:870px"><span class="eyebrow">WHO WE ARE</span></div>
<h2 class="abs center h2" style="top:906px;font-size:42px">Safe Workplaces, Better Outcomes</h2>
<p class="abs para" style="left:175px;top:976px;width:850px;text-align:center;font-size:13px;line-height:22px">Lorem ipsum dolor sit amet, consectetur adipiscing elit, sed do eiusmod tempor incididunt ut labore et dolore magna aliqua. Ut enim ad minim veniam, quis laboris nisi ut aliquip ex ea commodo consequat. Lorem ipsum dolor sit am et, consectetur adipiscing elit, sed do eiusmod te a</p>
<div class="abs card" style="left:152px;top:1084px">
  <svg width="56" height="56" viewBox="0 0 56 56"><circle cx="24" cy="22" r="6"/><path d="M20 10l10 6M30 26l6 10M8 48h40M14 44c6-10 18-10 24 0"/></svg>
  <h3>CLIENT-CENTRIC</h3>
</div>
<div class="abs card" style="left:462px;top:1084px;gap:18px">
  <h3>PROFESSIONAL</h3>
  <p>Lorem ipsum dolor sit amet, consectetur adipiscing elit, sed do eiusmod tempor incidid unt ut labore et dolore magna ali</p>
</div>
<div class="abs card" style="left:769px;top:1084px">
  <svg width="66" height="60" viewBox="0 0 66 60"><path d="M33 6L58 24 48 54H18L8 24Z"/><circle cx="33" cy="6" r="5" fill="#fff"/><circle cx="58" cy="24" r="5" fill="#fff"/><circle cx="48" cy="54" r="5" fill="#fff"/><circle cx="18" cy="54" r="5" fill="#fff"/><circle cx="8" cy="24" r="5" fill="#fff"/></svg>
  <h3>EXPERTISE</h3>
</div>

<!-- mitigating risks -->
<div class="abs" style="left:134px;top:1528px"><span class="eyebrow" style="font-size:12px">WHO WE ARE</span></div>
<h2 class="abs h2" style="left:134px;top:1565px;font-size:38px;line-height:47px">Mitigating Risks,<br>Ensuring <span style="color:var(--blue)">Safety</span></h2>
<h3 class="abs" style="left:134px;top:1680px;font-size:20px;font-weight:600;color:var(--ink)">Expert Guidance for a Safer Environment</h3>
<p class="abs para" style="left:134px;top:1726px;width:460px">Lorem ipsum dolor sit amet, consectetur adipiscing elit, sed do eiusmod temp or incididunt ut labore et dolore magna aliqua. Ut enim ad minim veniam, quis laboris nisi ut aliquip ex ea commodo consequat.</p>
<p class="abs para" style="left:134px;top:1788px;width:460px">Lorem ipsum dolor sit amet, consectetur adipiscing elit, sed do eiusmod temp or incididunt ut labore et dolore magna aliqua.</p>
<a class="abs btn" style="left:134px;top:1852px;width:134px;height:39px;border-radius:2px">Contact us &rarr;</a>
<div class="abs" style="left:650px;top:1486px;width:450px;height:440px;border-radius:50%;background:#f3f4e2"></div>
<div class="abs" role="img" aria-label="Photo of a site inspector in a hard hat pointing at a building under construction" style="left:642px;top:1493px;width:426px;height:426px;border-radius:50%;background:linear-gradient(160deg,#3d86d4,#8fb6dd 50%,#8a8676)"></div>
<div class="abs" role="img" aria-label="Photo of a technician checking aircraft landing gear" style="left:952px;top:1534px;width:200px;height:200px;border-radius:50%;background:linear-gradient(160deg,#d7dde2,#6b6e6e);border:4px solid #fff"></div>
<div class="abs" style="left:648px;top:1822px;width:94px;height:94px;border-radius:50%;background:var(--blue)"></div>

<!-- services strip -->
<div class="abs svc" role="img" aria-label="Photo of two safety workers in hard hats reviewing a tablet in a warehouse" style="left:0;width:342px;background:linear-gradient(150deg,#c7a27a,#e28a3a 60%,#3b4a5c)"></div>
<div class="abs svc band" style="left:342px;width:57px"><span class="vert"><b>Risk Assessments</b> Lorem ipsum dolor sit amet, consectetu &rarr;</span></div>
<div class="abs svc" role="img" aria-label="Photo of a safety audit team in hard hats in a warehouse aisle" style="left:399px;width:400px;background:linear-gradient(160deg,#8b97a6,#3e4a59)"></div>
<div class="abs svc" style="left:399px;width:400px;background:rgba(10,25,50,.35)"></div>
<div class="abs" style="left:438px;top:2312px;width:60px;height:60px;border-radius:50%;background:#fff;display:flex;align-items:center;justify-content:center">
  <svg width="30" height="30" viewBox="0 0 56 56" fill="none" stroke="#0e2a5a" stroke-width="4"><circle cx="24" cy="22" r="6"/><path d="M20 10l10 6M8 48h40M14 44c6-10 18-10 24 0"/></svg>
</div>
<div class="abs" style="left:438px;top:2382px;width:320px;color:#fff">
  <div style="font-weight:700;font-size:16px">Safety Audits</div>
  <p style="font-size:13px;line-height:20px">Lorem ipsum dolor sit amet, consectetur adipiscing elit, sed do eiusmod tempor incididunt ut labore et dolore magna aliqua. Ut enim ad minim</p>
  <div style="font-size:22px;margin-top:6px">&rarr;</div>
</div>
<div class="abs svc" role="img" aria-label="Photo of engineers in orange vests and hard hats reading a clipboard" style="left:799px;width:342px;background:linear-gradient(150deg,#6f7880,#e07a2c 65%,#9aa3ab)"></div>
<div class="abs svc band" style="left:1141px;width:59px"><span class="vert"><b>Incident Investigation</b> Lorem ipsum dolor sit amet, consectetu &rarr;</span></div>

<!-- testimonials -->
<section class="abs pale" style="left:0;top:2509px;width:1200px;height:644px"></section>
<div class="abs center" style="top:2574px;font-size:18px;color:var(--blue)">TESTIMONIALS</div>
<h2 class="abs center h2" style="top:2604px;font-size:32px">What Our Clients are <span style="color:var(--blue)">Saying</span></h2>
<svg class="abs" style="left:190px;top:2730px" width="830" height="170"><path d="M10 160 C100 80 250 30 415 10 C580 30 730 80 820 160" fill="none" stroke="#0677ba" stroke-width="2" stroke-dasharray="7 6"/></svg>
<div class="abs avatar" role="img" aria-label="Client portrait" style="left:543px;top:2680px;width:120px;height:120px"></div>
<div class="abs avatar" role="img" aria-label="Client portrait" style="left:347px;top:2738px;width:74px;height:74px"></div>
<div class="abs avatar" role="img" aria-label="Client portrait" style="left:788px;top:2738px;width:74px;height:74px"></div>
<div class="abs avatar" role="img" aria-label="Client portrait" style="left:161px;top:2854px;width:74px;height:74px"></div>
<div class="abs avatar" role="img" aria-label="Client portrait" style="left:972px;top:2854px;width:74px;height:74px"></div>
<div class="abs center" style="top:2822px;font-size:64px;font-weight:800;color:var(--blue);line-height:64px;font-family:Georgia,serif">&ldquo;</div>
<p class="abs center" style="top:2898px;font-size:17px;line-height:31px;color:#333a48;padding:0 290px">Lorem ipsum dolor sit amet, consectetur adipiscing elit, sed do eiusmod te dunt ut labore et dolore magna aliqua .dipiscing elit, sed do eiusmod temp dunt ut labore et dolore magna aliqua .dipiscing elit, sed</p>
<div class="abs arrow" style="left:466px;top:3022px;background:#123a2e;color:#fff">&larr;</div>
<div class="abs arrow" style="left:697px;top:3022px;background:var(--blue);color:#fff">&rarr;</div>
<div class="abs center" style="top:3004px;color:var(--star);font-size:18px;letter-spacing:2px">&#9733;&#9733;&#9733;&#9733;&#9733;</div>
<div class="abs center" style="top:3035px;color:var(--star);font-size:18px;font-weight:600">Marcus Hale</div>
<div class="abs center" style="top:3064px;font-size:11px;color:#333">Client</div>

<!-- contact -->
<h2 class="abs h2" style="left:140px;top:3278px;font-size:34px;line-height:44px;font-weight:600">Get &nbsp;in Touch<br><span style="color:var(--blue);font-weight:400">Contact Us</span></h2>
<p class="abs para" style="left:140px;top:3388px;width:380px;font-size:13px;line-height:22px">Lorem ipsum dolor sit amet, consectetur adipiscing e lit, sed do eiusmod tempor incididunt ut labore et dolore magna aliqua. ceptos ...</p>
<div class="abs" style="left:140px;top:3484px;width:380px;border-top:1.5px solid #d7dbe1"></div>
<div class="abs info" style="top:3515px"><i><svg width="14" height="18" viewBox="0 0 14 18"><path d="M7 0a7 7 0 0 0-7 7c0 5 7 11 7 11s7-6 7-11a7 7 0 0 0-7-7z" fill="#0677ba"/><circle cx="7" cy="7" r="2.5" fill="#fff"/></svg></i>Lindenweg 7, 5020 Talheim</div>
<div class="abs info" style="top:3577px"><i><svg width="16" height="16" viewBox="0 0 16 16"><path d="M3 1l3 3-2 2c1 2 3 4 6 6l2-2 3 3-2 2C7 15 1 9 1 3z" fill="#0677ba"/></svg></i>+43 1 5550 1842</div>
<div class="abs info" style="top:3632px"><i><svg width="16" height="12" viewBox="0 0 16 12"><rect width="16" height="12" rx="2" fill="#0e2a5a"/><path d="M1 1l7 6 7-6" stroke="#fff" fill="none" stroke-width="1.5"/></svg></i>office@kestrelvi.com</div>

<div class="abs" style="left:588px;top:3218px;width:486px;height:545px;background:#fff;border-top:3px solid var(--blue);border-radius:6px;box-shadow:0 6px 24px rgba(20,50,90,.12)"></div>
<div class="abs field-label" style="left:624px;top:3265px">Full Name:</div>
<div class="abs field" style="left:620px;top:3298px;width:422px;height:42px">Sed non neque elit.</div>
<div class="abs field-label" style="left:624px;top:3369px">Email :</div>
<div class="abs field-label" style="left:850px;top:3369px">Phone no :</div>
<div class="abs field" style="left:620px;top:3401px;width:196px;height:43px">Sed non neque elit.</div>
<div class="abs field" style="left:846px;top:3401px;width:196px;height:43px">Sed non neque elit.</div>
<div class="abs field-label" style="left:624px;top:3479px">Messages &nbsp;:</div>
<div class="abs field" style="left:620px;top:3511px;width:422px;height:128px">Sed non neque elit.</div>
<a class="abs btn" style="left:618px;top:3667px;width:126px;height:40px">SUBMIT</a>

<!-- footer -->
<svg class="abs" style="left:0;top:3780px" width="1200" height="540" viewBox="0 0 1200 540">
  <path d="M0 240 C300 120 700 70 1200 80 L1200 540 L0 540Z" fill="#163150"/>
  <path d="M380 96 C650 40 950 20 1200 10 L1200 40 C900 40 640 70 380 96Z" fill="#0677ba"/>
</svg>
<div class="abs brand" style="left:456px;top:4020px"><span class="mark" style="width:40px;height:40px;background:#fff"></span><span class="name" style="color:#fff;font-size:44px">Kestrel</span></div>
<p class="abs foot-t" style="left:455px;top:4104px;width:290px;text-align:center">Lorem ipsum dolor sit amet, consectetur adipisc ing elit, sed do eiusmod tempor incididunt ut lab bcbbcbnmx zjzmsmmzm</p>
<div class="abs" style="left:535px;top:4187px;display:flex;gap:8px"><div class="soc"><span></span></div><div class="soc"><span></span></div><div class="soc"><span></span></div></div>

<div class="abs foot-h" style="left:94px;top:4060px">CONTACT US</div>
<div class="abs foot-t" style="left:94px;top:4098px;width:250px;display:flex;gap:18px"><span>&#9679;</span><span>22 Marlow Street, suite 4<br>print type text industry text.</span></div>
<div class="abs foot-t" style="left:94px;top:4157px;display:flex;gap:18px"><span>&#9742;</span><span>555 014 2290</span></div>
<div class="abs foot-t" style="left:94px;top:4194px;display:flex;gap:18px"><span>&#9993;</span><span>info@kestrelvi.com</span></div>

<div class="abs foot-h" style="left:972px;top:4060px">OPENING HOURS</div>
<div class="abs foot-t" style="right:90px;top:4104px;text-align:right;line-height:31px">Mon - Fri: 9am - to - 6pm &nbsp;&#9719;<br>Saturday 9am - to - 2pm &nbsp;&#9719;<br>Sunday : <u>Closed</u> &nbsp;&#9719;</div>

<div class="abs" style="left:64px;top:4254px;width:1072px;border-top:1px solid #3a5572"></div>
<div class="abs center foot-t" style="top:4280px">Kestrel</div>

</body>
</html>
```